Business Card Design Project

Business card design with a funky, clean, modern design. Business is an immigration consultancy. Client base will be Canadian employers wanting to hire or retain foreign workers and foreign nationals wanting to immigrate to Canada.

Full color possible, but should incorporate red/white/black as per the logo to be provided. Double sided card design.

Target Market(s)

Canadian employers looking to hire/retain staff and also foreign nationals immigrating to Canada

Industry/Entity Type

Business

Requirements
Must have
• Logo (to be provided)
Name (Marla Voskuil, Immigration Consultant)
Phone (604) 731-5562
E-mail: marla@tallowbrookmigration.example
Web: www.tallowbrookmigration.example

Nice to have
• Tag Line
Clean, modern style

```html
<!DOCTYPE html>
<html lang="en">
<head>
<meta charset="utf-8">
<title>Tallowbrook Migration — Business Card</title>
<link rel="stylesheet" href="https://fonts.googleapis.com/css2?family=Tinos:wght@400;700&display=swap">
<style>
  :root {
    --brand-red: #e00000;
    --brand-red-deep: #c40000;
    --card-white: #ffffff;
    --ink: #1a1a1a;
    --rule-red: #e88a8a;
    --backdrop-light: #d9d9d9;
    --backdrop-dark: #9a9a9a;
  }
  * { box-sizing: border-box; margin: 0; padding: 0; }
  html, body {
    width: 1200px;
    height: 900px;
    overflow: hidden;
  }
  body {
    background: radial-gradient(ellipse at 55% 60%, var(--backdrop-light) 0%, #c4c4c4 55%, var(--backdrop-dark) 100%);
    font-family: "Tinos", "Times New Roman", serif;
    position: relative;
  }
  .card {
    position: absolute;
    left: 350px;
    width: 500px;
    height: 286px;
    box-shadow: 0 10px 28px rgba(0,0,0,0.28);
  }

  /* Front side */
  .card-front {
    top: 120px;
    background: var(--brand-red);
    overflow: hidden;
  }
  .card-front .front-glow {
    position: absolute;
    inset: 0;
    background: radial-gradient(circle at 30% 40%, rgba(255,255,255,0.10) 0%, rgba(255,255,255,0.04) 40%, rgba(0,0,0,0) 65%);
  }
  .front-wordmark {
    position: absolute;
    left: 0; right: 0;
    top: 50%;
    transform: translateY(-50%);
    display: flex;
    flex-direction: column;
    align-items: center;
    gap: 10px;
    color: var(--card-white);
    font-weight: 700;
    text-align: center;
  }
  .front-wordmark .mark-dot {
    width: 46px; height: 46px;
    border-radius: 50%;
    background: var(--card-white);
  }
  .front-wordmark .name-line {
    font-size: 26px;
    letter-spacing: 1px;
    line-height: 1;
  }
  .front-wordmark .sub-line {
    font-size: 12px;
    letter-spacing: 3px;
    line-height: 1;
  }

  /* Back side */
  .card-back {
    top: 480px;
    background: var(--card-white);
  }
  .back-wordmark {
    position: absolute;
    left: 30px;
    top: 0; bottom: 0;
    width: 180px;
    display: flex;
    flex-direction: column;
    align-items: center;
    justify-content: center;
    gap: 8px;
    color: var(--ink);
    font-weight: 700;
    text-align: center;
  }
  .back-wordmark .mark-dot {
    width: 38px; height: 38px;
    border-radius: 50%;
    background: var(--brand-red);
  }
  .back-wordmark .name-line { font-size: 19px; letter-spacing: 0.5px; line-height: 1; }
  .back-wordmark .sub-line { font-size: 9px; letter-spacing: 2.5px; line-height: 1; }

  .divider {
    position: absolute;
    left: 232px;
    top: 40px;
    bottom: 40px;
    width: 1px;
    background: var(--rule-red);
  }
  .holder {
    position: absolute;
    left: 262px;
    top: 46px;
    color: var(--ink);
  }
  .holder .holder-name { font-size: 22px; line-height: 1.1; }
  .holder .holder-title { font-size: 12px; margin-top: 2px; }

  .contact-list {
    position: absolute;
    left: 248px;
    top: 176px;
    list-style: none;
    color: var(--ink);
    font-size: 13px;
  }
  .contact-list li {
    display: flex;
    align-items: center;
    gap: 8px;
    height: 21px;
  }
  .contact-list svg { width: 9px; height: 9px; flex: none; }

  .edge-tab {
    position: absolute;
    right: 0;
    top: 50px;
    width: 14px;
    height: 30px;
  }
</style>
</head>
<body>

  <section class="card card-front" aria-label="Card front">
    <div class="front-glow"></div>
    <div class="front-wordmark">
      <span class="mark-dot"></span>
      <span class="name-line">TALLOWBROOK</span>
      <span class="sub-line">MIGRATION</span>
    </div>
  </section>

  <section class="card card-back" aria-label="Card back">
    <div class="back-wordmark">
      <span class="mark-dot"></span>
      <span class="name-line">TALLOWBROOK</span>
      <span class="sub-line">MIGRATION</span>
    </div>

    <div class="divider"></div>

    <div class="holder">
      <div class="holder-name">Marla Voskuil</div>
      <div class="holder-title">RCIC</div>
    </div>

    <ul class="contact-list">
      <li>
        <svg viewBox="0 0 10 10" aria-hidden="true"><rect x="2.5" y="0.5" width="5" height="9" rx="1" fill="none" stroke="#e00000" stroke-width="1.2"/></svg>
        (604) 731-5562
      </li>
      <li>
        <svg viewBox="0 0 10 10" aria-hidden="true"><rect x="0.6" y="2" width="8.8" height="6" fill="none" stroke="#e00000" stroke-width="1.1"/><path d="M0.6 2 L5 5.5 L9.4 2" fill="none" stroke="#e00000" stroke-width="1"/></svg>
        marla@tallowbrookmigration.example
      </li>
      <li>
        <svg viewBox="0 0 10 10" aria-hidden="true"><circle cx="5" cy="5" r="4.4" fill="#e00000"/><path d="M0.8 5 H9.2 M5 0.6 V9.4" stroke="#fff" stroke-width="0.7"/></svg>
        www.tallowbrookmigration.example
      </li>
    </ul>

    <svg class="edge-tab" viewBox="0 0 14 30" aria-hidden="true"><polygon points="14,0 0,15 14,30" fill="var(--brand-red)"/></svg>
  </section>

</body>
</html>
```